Broschüre für Bauingenieurbüro
Zielgruppe
Wir sind ein kleines Bauingenieurbüro mit bis 10 Mitarbeiterinnen. Wir wollen uns bei bestehenden Kunden mit der Broschüre in Erinnerung rufen und für neue Kunden genügend Informationen und Schlagkraft aufzeigen, dass diese uns Aufträge zukommen lassen. Zu unseren Kunden gehören hauptsächlich Architekturbüros und wenige Privatpersonen als Bauherren.
Aufgabenstellung
Wir möchten die Broschüre auf A3 doppelseitig mit einem Falz in der Mitte haben (Zusammengefaltet soll die Broschüre das Format A4 aufweisen). Unser bestehendes Porträt wird dem Auftrag beigelegt (PDF Rohversion Seite 3 und 4). Das Dokument 'Veränderung Firmenporträt 220818' zeigt unsere Wünsche auf. Das Design der Broschüre soll dann in einem weiteren Schritt auch auf die Homepage übergehen.

```html
<!DOCTYPE html>
<html lang="de">
<head>
<meta charset="utf-8">
<title>Kurzportrait – kernwerk bauingenieure</title>
<link rel="stylesheet" href="https://fonts.googleapis.com/css2?family=Work+Sans:wght@300;400;500;600&display=swap">
<style>
:root{
  --bg:#e4e5e7;
  --paper:#f1f1f1;
  --ink:#3a3a3a;
  --ink-soft:#6b6b6b;
  --grid:#cfcfcf;
  --tan:#c2b39a;
  --dark:#4a4a4a;
  --photo-a:#c9cdd0;
  --photo-b:#a9b3a6;
}
*{box-sizing:border-box;margin:0;padding:0}
html,body{width:1200px;height:2592px;overflow:hidden;background:var(--bg);font-family:"Work Sans",sans-serif;color:var(--ink)}
.scene{position:relative;width:1200px;height:864px}
.spread{position:absolute;left:180px;top:135px;width:840px;height:594px;display:flex;box-shadow:0 18px 40px rgba(0,0,0,.12)}
.page{position:relative;width:420px;height:594px;background-color:var(--paper);overflow:hidden;
  background-image:linear-gradient(var(--grid) 1px,transparent 1px),linear-gradient(90deg,var(--grid) 1px,transparent 1px);
  background-size:60px 66px;background-position:30px 33px}
.page + .page{border-left:1px solid #dcdcdc}
.abs{position:absolute}
.display{font-weight:400;letter-spacing:.12em;text-transform:uppercase;line-height:1}
.tiny{font-size:6.5px;line-height:1.35;color:var(--ink-soft)}
.photo{position:absolute;border:1px solid #fff}
.arrow{position:absolute}

/* back cover */
.ref-title{left:-40px;top:330px;font-size:34px;transform:rotate(-90deg);transform-origin:left top;white-space:nowrap}
.ref-caption{writing-mode:vertical-rl;font-size:6px;color:var(--ink-soft)}
.address{left:150px;top:470px;font-size:15px;letter-spacing:.06em;line-height:1.2;text-transform:uppercase;background:var(--paper);padding:2px 4px}
.ref-note{left:28px;top:560px;font-size:6.5px;color:var(--ink-soft)}

/* front covers */
.kp-title{font-size:46px;letter-spacing:.1em}
.tagline{font-size:15px;letter-spacing:.14em;line-height:1.25;text-transform:uppercase;text-align:right}
.brand{display:flex;align-items:center;gap:6px;font-size:18px;font-weight:400;color:var(--ink-soft);letter-spacing:.04em}
.brand .mark{width:12px;height:12px;background:var(--tan)}

/* inside */
.h-inside{font-size:30px;letter-spacing:.1em}
.body{font-size:7px;line-height:1.45;color:var(--ink)}
.body b{font-weight:600}
.cells{position:absolute;display:grid;grid-template-columns:repeat(4,80px);grid-auto-rows:46px;border-top:1px solid #9a9a9a}
.cells div{font-size:6.5px;line-height:1.3;padding:5px 4px;border-right:1px solid #bdbdbd;border-bottom:1px solid #bdbdbd;background:var(--paper)}
.comp h4{font-size:6.5px;font-weight:600;margin-top:6px}
.comp p{font-size:6px;color:var(--ink-soft)}
</style>
</head>
<body>

<!-- spread 1: back cover + front cover with photo -->
<section class="scene">
  <div class="spread">
    <div class="page back-cover">
      <svg class="arrow" style="left:40px;top:60px" width="40" height="14"><line x1="0" y1="7" x2="38" y2="7" stroke="#3a3a3a"/><polyline points="32,2 38,7 32,12" fill="none" stroke="#3a3a3a"/></svg>
      <div class="abs display ref-title">Referenzen</div>
      <div class="photo" role="img" aria-label="Referenzfoto: moderne Villa mit Pool" style="left:120px;top:40px;width:170px;height:88px;background:linear-gradient(160deg,#e8ecef,#b9c3c7 60%,#8fa39a)"></div>
      <div class="abs ref-caption" style="left:296px;top:40px">Neubau Villa am Hang</div>
      <div class="photo" role="img" aria-label="Referenzfoto: Wohnhaus mit dunklem Dach" style="left:220px;top:128px;width:170px;height:100px;background:linear-gradient(170deg,#bcd0e4,#5a5e62 45%,#d9d6cf 70%,#7f9262)"></div>
      <div class="abs ref-caption" style="left:200px;top:130px">Umbau Wohnhaus Dachgeschoss</div>
      <div class="photo" role="img" aria-label="Referenzfoto: historisches Schlossgebäude" style="left:150px;top:250px;width:170px;height:110px;background:linear-gradient(170deg,#9ec2de,#d8d2c2 45%,#6f8a55)"></div>
      <div class="abs ref-caption" style="left:326px;top:252px">Sanierung Schloss Ostflügel</div>
      <div class="abs address">Lindenhofweg 18,<br>8400 Winterthur<br>(+41) 52 555 01 23<br>info@kernwerk-ing.ch</div>
      <div class="abs ref-note">Weitere Referenzen finden Sie auf unserer Website.</div>
    </div>
    <div class="page front-cover">
      <div class="abs" style="left:300px;top:24px;width:18px;height:18px;background:var(--dark)"></div>
      <div class="abs tiny" style="left:30px;top:30px">kernwerk-ing.ch</div>
      <div class="photo" role="img" aria-label="Architekturfoto: Betonfassade und Stahlkonstruktion" style="left:40px;top:60px;width:250px;height:230px;border-radius:0 0 0 120px;background:linear-gradient(135deg,#5c5c5c,#d4d4d4 45%,#f0f0f0 70%,#8a8a8a)"></div>
      <svg class="arrow" style="left:340px;top:110px" width="14" height="40"><line x1="7" y1="2" x2="7" y2="40" stroke="#3a3a3a"/><polyline points="2,8 7,2 12,8" fill="none" stroke="#3a3a3a"/></svg>
      <div class="abs display kp-title" style="left:70px;top:330px">Kurz-<br>portrait</div>
      <div class="abs tagline" style="right:28px;top:470px">Mit uns findet<br>Ihre Vision<br>die notwendige<br>Stabilität</div>
    </div>
  </div>
</section>

<!-- spread 2: back cover + typographic front cover -->
<section class="scene">
  <div class="spread">
    <div class="page back-cover">
      <svg class="arrow" style="left:40px;top:60px" width="40" height="14"><line x1="0" y1="7" x2="38" y2="7" stroke="#3a3a3a"/><polyline points="32,2 38,7 32,12" fill="none" stroke="#3a3a3a"/></svg>
      <div class="abs display ref-title">Referenzen</div>
      <div class="photo" role="img" aria-label="Referenzfoto: moderne Villa mit Pool" style="left:120px;top:40px;width:170px;height:88px;background:linear-gradient(160deg,#e8ecef,#b9c3c7 60%,#8fa39a)"></div>
      <div class="abs ref-caption" style="left:296px;top:40px">Neubau Villa am Hang</div>
      <div class="photo" role="img" aria-label="Referenzfoto: Wohnhaus mit dunklem Dach" style="left:220px;top:128px;width:170px;height:100px;background:linear-gradient(170deg,#bcd0e4,#5a5e62 45%,#d9d6cf 70%,#7f9262)"></div>
      <div class="abs ref-caption" style="left:200px;top:130px">Umbau Wohnhaus Dachgeschoss</div>
      <div class="photo" role="img" aria-label="Referenzfoto: historisches Schlossgebäude" style="left:150px;top:250px;width:170px;height:110px;background:linear-gradient(170deg,#9ec2de,#d8d2c2 45%,#6f8a55)"></div>
      <div class="abs ref-caption" style="left:326px;top:252px">Sanierung Schloss Ostflügel</div>
      <div class="abs address">Lindenhofweg 18,<br>8400 Winterthur<br>(+41) 52 555 01 23<br>info@kernwerk-ing.ch</div>
      <div class="abs ref-note">Weitere Referenzen finden Sie auf unserer Website.</div>
    </div>
    <div class="page front-cover">
      <div class="abs display kp-title" style="left:30px;top:40px">Kurz-<br>portrait</div>
      <svg class="abs" style="left:0;top:120px" width="420" height="40"><path d="M0 30 Q210 -10 420 30" fill="none" stroke="#9a9a9a"/></svg>
      <svg class="arrow" style="left:200px;top:175px" width="14" height="40"><line x1="7" y1="0" x2="7" y2="38" stroke="#3a3a3a"/><polyline points="2,32 7,38 12,32" fill="none" stroke="#3a3a3a"/></svg>
      <div class="abs tagline" style="right:28px;top:380px">Mit uns findet<br>Ihre Vision<br>die notwendige<br>Stabilität</div>
      <div class="abs brand" style="left:30px;top:540px"><span class="mark"></span>kernwerk</div>
    </div>
  </div>
</section>

<!-- spread 3: inside pages -->
<section class="scene">
  <div class="spread">
    <div class="page inside-left">
      <div class="abs display h-inside" style="left:34px;top:70px">Das sind<br>wir</div>
      <div class="abs body" style="left:34px;top:160px;width:250px">
        Die kernwerk bauingenieure gmbh ist ein unabhängiges, junges und dynamisches Ingenieurbüro mit Sitz in Winterthur. Wir planen Tragwerke für Neubauten, Umbauten und Sanierungen im Hoch- und Tiefbau.<br><br>
        <b>Zu unseren häufigsten Bauobjekten gehören:</b><br>
        Wohnungsbauten<br>Gewerbe- und Industriebauten<br>Öffentliche Bauten<br>Pflegeheime<br>Landwirtschaftliche Bauten<br>Kunstbauten<br>Stützmauern<br>Balkonanbauten<br>Schwimmbäder
      </div>
      <div class="cells" style="left:100px;top:380px">
        <div></div><div>Projektbearbeitung auf Wunsch in Deutsch und Englisch</div><div>Fundiertes Fachwissen und kreative Lösungen</div><div></div>
        <div>Laufende Aus- &amp; Weiterbildung aller Mitarbeitenden</div><div>In der gesamten Deutschschweiz in Ihrer Nähe tätig</div><div>Engagiertes &amp; dynamisches Team für Hochbauprojekte</div><div></div>
        <div>Praxisnahes Planen auf dem neuesten Stand der Technik</div><div>Täglich Einblicke in alle Facetten des Hochbaus</div><div></div><div></div>
        <div>Schlank, optimal auf Ihr Bauprojekt ausgerichtet</div><div></div><div></div><div></div>
      </div>
      <div class="abs" style="left:34px;top:500px;width:62px;height:62px;background:var(--tan)"></div>
    </div>
    <div class="page inside-right">
      <div class="abs" style="right:0;top:40px;width:46px;height:250px;background:var(--dark)"></div>
      <div class="abs" style="left:30px;top:46px;font-size:12px;letter-spacing:.12em;line-height:1.2;text-transform:uppercase">Klassischer Ingenieur<br>Hochbau … unser Beitrag<br>an Ihr Bauwerk</div>
      <div class="abs display h-inside" style="left:30px;top:100px">Kompetenzen</div>
      <div class="abs comp" style="left:150px;top:150px;width:210px">
        <h4>Tragwerksplanung</h4><p>Beton-, Stahl- &amp; Holzbau</p>
        <h4>Tragwerksanalyse | Tragwerksverstärkung</h4><p>Zustandsbeurteilung | Statische Nachweise</p>
        <h4>Baugruben | Baugrubenüberwachung</h4><p>Aushub | Baugrubenabschlüsse | Nachbarparzellen</p>
        <h4>Leistungskatalog</h4><p>Abbruch | Umbau &amp; Aufstockung | Sanierung</p>
        <h4>Baupläne</h4><p>Schalungs- &amp; Bewehrungspläne | Stahlbaupläne</p>
        <h4>Digitalisierung | BIM</h4><p>Tragwerksmodell | Qualitätssicherung</p>
        <h4>Drohnenflüge</h4><p>Vermessung | Fassaden | Dächer</p>
      </div>
      <svg class="arrow" style="left:70px;top:250px" width="14" height="40"><line x1="7" y1="0" x2="7" y2="38" stroke="#3a3a3a"/><polyline points="2,32 7,38 12,32" fill="none" stroke="#3a3a3a"/></svg>
      <div class="abs" style="left:150px;top:430px;width:230px;border-top:1px solid #9a9a9a;padding-top:6px">
        <div style="font-size:11px;letter-spacing:.12em;line-height:1.25;text-transform:uppercase">Berufsbildung … unser<br>Beitrag an die Zukunft</div>
        <p class="tiny" style="margin-top:6px">Lernende Zeichner/in Fachrichtung Ingenieurbau EFZ<br>Ausbildung Lernende</p>
      </div>
    </div>
  </div>
</section>

</body>
</html>
```